Kestrel Property Management email template

Looking for an email template for communications sent to residents that reads well in most email formats including mobile devices. Similar to the attached email, not quite reclaimed wood but something warm with interesting texture

```html
<!DOCTYPE html>
<html lang="en">
<head>
<meta charset="utf-8">
<title>Kestrel Property Management – Fall Maintenance Email</title>
<link rel="stylesheet" href="https://fonts.googleapis.com/css2?family=Hind:wght@400;600;700&family=Arimo:wght@400&display=swap">
<style>
  :root {
    --stage: #333333;
    --wood-dark: #1e0f06;
    --wood-mid: #8a5a2a;
    --wood-glow: #d79a55;
    --wood-edge: #7a3a10;
    --card: #ffffff;
    --navy: #1b2554;
    --navy-deep: #141c45;
    --ice: #e8eef9;
    --gold: #c49a5a;
    --link: #3a5ea8;
    --ink: #1a1a1a;
  }
  * { box-sizing: border-box; margin: 0; padding: 0; }
  html, body { width: 1200px; height: 1200px; overflow: hidden; background: var(--stage); }
  .canvas { position: relative; width: 1200px; height: 1200px; }
  .email-backdrop {
    position: absolute; left: 358px; top: 196px; width: 480px; height: 800px;
    background:
      radial-gradient(ellipse 55% 35% at 50% 100%, rgba(240,180,110,.85), transparent 70%),
      linear-gradient(90deg, rgba(0,0,0,.35), transparent 20%, transparent 80%, rgba(0,0,0,.35)),
      linear-gradient(180deg, var(--wood-dark) 0%, #2a1408 22%, var(--wood-mid) 50%, #a8692e 75%, var(--wood-edge) 100%);
  }
  .email-card {
    position: absolute; left: 422px; top: 224px; width: 351px; height: 740px;
    background: var(--card); border-radius: 6px; overflow: hidden;
    box-shadow: 0 4px 18px rgba(0,0,0,.35);
  }
  .brand-header { height: 122px; display: flex; align-items: center; padding-left: 28px; gap: 10px; }
  .brand-mark { width: 14px; height: 14px; background: var(--navy); }
  .brand-name { font-family: "Hind", sans-serif; font-weight: 700; font-size: 15px; color: var(--navy); letter-spacing: .1px; }
  .hero-photo {
    height: 169px;
    background:
      radial-gradient(ellipse 40% 60% at 18% 20%, rgba(250,230,150,.95), transparent 70%),
      linear-gradient(180deg, #9a7a3a 0%, #a8652c 45%, #6e4a24 70%, #c48a62 100%);
  }
  .headline-band { height: 107px; background: var(--ice); text-align: center; padding-top: 20px; }
  .headline { font-family: "Hind", sans-serif; font-weight: 700; font-size: 23px; line-height: 25px; color: var(--navy-deep); }
  .subhead { font-family: "Hind", sans-serif; font-weight: 400; font-size: 17px; line-height: 22px; color: var(--ink); margin-top: 2px; }
  .cta-band { height: 64px; background: var(--gold); display: flex; align-items: center; justify-content: center; text-align: center; }
  .cta-text { font-family: "Hind", sans-serif; font-weight: 700; font-size: 18.5px; line-height: 22px; color: #fff; }
  .body-columns { height: 180px; background: var(--ice); display: flex; gap: 24px; padding: 20px 26px 0 26px; border-radius: 0 0 6px 6px; }
  .body-columns p { flex: 1; font-family: "Arimo", sans-serif; font-size: 9.2px; line-height: 10.4px; color: var(--ink); }
  .fine-print { padding: 11px 31px 0 26px; font-family: "Arimo", sans-serif; font-size: 5.6px; line-height: 6.9px; color: var(--ink); text-align: justify; }
  .site-link { display: block; text-align: center; margin-top: 20px; font-family: "Hind", sans-serif; font-size: 17px; color: var(--link); letter-spacing: .5px; text-decoration: none; }
</style>
</head>
<body>
<div class="canvas">
  <div class="email-backdrop"></div>
  <main class="email-card">
    <header class="brand-header">
      <span class="brand-mark"></span>
      <span class="brand-name">KESTREL PROPERTY MANAGEMENT</span>
    </header>
    <div class="hero-photo" role="img" aria-label="Sunlit autumn avenue lined with orange-leaved trees"></div>
    <section class="headline-band">
      <h1 class="headline">FALL MAINTENANCE<br>AND PREPARATION IS KEY</h1>
      <p class="subhead">to peace of mind come Winter</p>
    </section>
    <section class="cta-band">
      <p class="cta-text">LET US HELP YOU BE PREPARED<br>AND AT PEACE.</p>
    </section>
    <section class="body-columns">
      <p>Mauris purus. Donec est nunc, ornare non, aliquet non, tempus vel, dolor. Integer sapien nibh, egestas ut, cursus sit amet, faucibus a, sapien. Vestibulum purus purus, elementum ac, luctus ullamcorper, ornare vitae, massa. Nullam posuere sem ut mauris. Nullam velit. Quisque sodales. Donec suscipit suscipit erat. Nam blandit. Praesent congue lorem non dolor. Maecenas vitae erat. Ut ac purus vel purus dapibus gravida.</p>
      <p>Mauris purus. Donec est nunc, ornare non, aliquet non, tempus vel, dolor. Integer sapien nibh, egestas ut, cursus sit amet, faucibus a, sapien. Vestibulum purus purus, elementum ac, luctus ullamcorper, ornare vitae, massa. Nullam posuere sem ut mauris. Nullam velit. Quisque sodales. Donec suscipit suscipit erat. Nam blandit. Praesent congue lorem non dolor. Maecenas vitae erat. Ut ac purus vel purus dapibus gravida.</p>
    </section>
    <p class="fine-print">You are receiving this message because you are a resident of a community managed by Kestrel Property Management. Seasonal maintenance visits are scheduled in advance and notices will be posted in each building. For questions about your unit, service requests or upcoming inspections, please contact the management office during regular business hours. Thank you.</p>
    <a class="site-link" href="#">kestrelmanagement.net</a>
  </main>
</div>
</body>
</html>
```